Web Page Design (Coded). Winner can expect additional work to implement

My current employer (www.harbinfield.com.au) requires the establishment of a new web page (www.harbinbluetorch.com.au) to promote safety and environmental products which will be sold to the oil / gas / mining and environmental sectors. The web page needs to be somehow aligned with the parent company page above (if only the colouring to appease my boss), yet innovate and awesome. The successful designer will be expected to provide coded files and be able to provide additional services to edit and launch the website. The website is currently operational but the content and format are both poor. The website will be predominantly based around promoting our products but will include a "buy online" section for some products which will be part of the website, but on a different tab / layer. Video's and flash will be part of the successful web page. Actually, I know very little about web pages so just go for gold and make it good and make it work. I am not adding any files at this point in time, but do post a message if you require any files.

Target Market(s)

Our products will be promoted to customers in Australia and SE Asia in the mining, oil and gas sectors predominantly with local government also a purchaser. Most purchase decisions will be made by males and people needing to solve problems quickly. They often won't care what product they receive as long as it does the job.

Industry/Entity Type

Safety

Requirements
Must have
• Must be aligned with our parent company page design (www.harbinfield.com.au). When I say aligned, I am talking effectively about fonts and colouring. The page design itself can be innovative beyond the parent company page design.
Somewhere on the page it must say we are a division of Harbinfield Pty Ltd.
Nice to have
• Easy to find products, read about them and download brochures. Links to be provided to "buy online" or "request a quote" next to each product, but without pricing.
It is essential that contacting us by phone, email etc... is easy to find through every layer of the page. This is essential. We would like some photo's on the home page scrolling through products, but these do not need to be large. Our current website (harbinbluetorch.com.au) has photo's but they are too big.

```html
<!DOCTYPE html>
<html lang="en">
<head>
<meta charset="utf-8">
<title>Harbin Blue Torch</title>
<link rel="stylesheet" href="https://fonts.googleapis.com/css2?family=Carlito:wght@400;700&family=Open+Sans:wght@400;600;700&display=swap">
<style>
  :root {
    --gold: #e6b50a;
    --gold-text: #dca514;
    --ink: #2f2f2f;
    --muted: #5a5a5a;
    --panel: #f0f0f0;
    --line: #e0e0e0;
    --navy: #0c2250;
    --navy-logo: #14285a;
    --hero-top: #5d7592;
    --hero-mid: #9fb2c6;
    --hero-sea: #c9d4de;
    --hero-sand: #3d4650;
    --label-bg: rgba(85, 92, 104, 0.85);
  }
  * { box-sizing: border-box; margin: 0; padding: 0; }
  html, body { width: 882px; height: 1200px; overflow: hidden; background: #fff; }
  body { position: relative; font-family: "Carlito", "Open Sans", sans-serif; color: var(--ink); }
  .abs { position: absolute; }

  /* header */
  .brand { left: 97px; top: 28px; color: var(--navy-logo); font-family: "Open Sans", sans-serif; font-weight: 700; font-size: 22px; line-height: 1; letter-spacing: -0.3px; }
  .brand small { display: block; font-size: 10.5px; letter-spacing: 0.6px; margin-top: 4px; }
  .search { left: 646px; top: 14px; width: 138px; height: 25px; background: #f2f2f2; }
  .search svg { position: absolute; right: 9px; top: 7px; }
  .nav { top: 54px; left: 449px; display: flex; font-family: "Open Sans", sans-serif; font-size: 10px; color: #333; }
  .nav a { color: inherit; text-decoration: none; display: block; height: 25px; line-height: 25px; }
  .nav .current { border: 2px solid var(--gold); color: var(--gold); width: 55px; text-align: center; line-height: 21px; margin-right: 22px; }
  .nav .item { margin-right: 20px; }

  /* hero */
  .hero { left: 0; top: 96px; width: 882px; height: 385px; background: linear-gradient(180deg, var(--hero-top) 0%, var(--hero-mid) 45%, var(--hero-sea) 62%, #b9c6d2 78%, var(--hero-sand) 100%); }
  .hero-figure { left: 170px; top: 122px; width: 170px; height: 340px; background: linear-gradient(180deg, rgba(30,34,42,0.55), rgba(25,28,34,0.75)); border-radius: 60px 60px 10px 10px; }
  .hero-label { background: var(--label-bg); color: #fff; font-weight: 700; font-size: 27px; line-height: 35px; padding: 0 14px; letter-spacing: 0.3px; }
  .hero-label.one { left: 407px; top: 202px; }
  .hero-label.two { left: 407px; top: 245px; }
  .quote-btn { left: 406px; top: 300px; width: 152px; height: 32px; background: var(--gold); display: flex; color: #333; font-size: 13px; }
  .quote-btn .ico { width: 35px; border-right: 1px solid rgba(0,0,0,0.15); display: flex; align-items: center; justify-content: center; }
  .quote-btn .txt { flex: 1; display: flex; align-items: center; padding-left: 10px; }

  .dots { top: 496px; left: 415px; display: flex; gap: 5px; }
  .dots span { width: 9px; height: 9px; border-radius: 50%; background: #d9d9d9; }
  .dots span.on { background: var(--gold); }

  /* welcome */
  .section-title { font-size: 22px; color: #333; font-weight: 400; }
  .section-title em { font-style: normal; color: var(--gold-text); }
  .welcome-title { left: 97px; top: 552px; }
  .welcome-copy { left: 97px; top: 594px; width: 450px; font-family: "Open Sans", sans-serif; font-size: 8.6px; line-height: 17.6px; color: var(--muted); }
  .btn { background: var(--gold); color: #333; font-size: 12.5px; display: flex; align-items: center; justify-content: center; border-bottom: 1px solid #c99b00; }
  .download-btn { left: 94px; top: 698px; width: 151px; height: 36px; gap: 6px; }

  .sectors { left: 574px; top: 539px; width: 200px; height: 190px; background: var(--panel); padding: 15px 15px 0 15px; }
  .sectors h3 { font-size: 21px; font-weight: 400; display: flex; align-items: center; gap: 10px; margin-bottom: 10px; }
  .sectors h3 em { font-style: normal; color: var(--gold-text); }
  .sectors ul { list-style: none; }
  .sectors li { font-size: 11.5px; height: 23px; line-height: 23px; border-bottom: 1px solid var(--line); padding-left: 18px; position: relative; color: #333; }
  .sectors li:last-child { border-bottom: 0; }
  .sectors li::before { content: ""; position: absolute; left: 3px; top: 10px; width: 4px; height: 4px; border-radius: 50%; background: #333; }

  .divider { left: 96px; top: 759px; width: 684px; height: 1px; background: var(--line); }

  /* products */
  .featured-title { left: 97px; top: 785px; }
  .featured-sub { left: 97px; top: 817px; font-size: 13px; color: #444; }
  .pager { top: 806px; display: flex; }
  .pager span { width: 17px; height: 17px; display: flex; align-items: center; justify-content: center; }
  .pager .prev { left: 750px; background: #eee; position: absolute; }
  .pager .next { left: 768px; background: #666; position: absolute; }

  .card { top: 850px; width: 162px; height: 220px; background: var(--panel); border-bottom: 2px solid #ddd; text-align: center; }
  .card .photo { margin: 12px auto 0; width: 142px; height: 91px; }
  .card h4 { font-size: 12.5px; font-weight: 400; margin-top: 13px; color: #222; letter-spacing: 0.3px; }
  .card p { font-family: "Open Sans", sans-serif; font-size: 8.6px; line-height: 15px; color: var(--muted); margin-top: 6px; padding: 0 8px; }
  .card .buy { width: 76px; height: 28px; margin: 12px auto 0; font-size: 11px; }
  .photo.sirens { background: linear-gradient(180deg, #4b8fd0, #3f86c8); }
  .photo.signage { background: linear-gradient(180deg, #f3f3f3 0%, #c2a14a 45%, #6a5a2e 100%); }
  .photo.cameras { background: linear-gradient(180deg, #7c8a5e 0%, #9aa486 45%, #5a5e56 100%); }
  .photo.monitoring { background: linear-gradient(180deg, #ffffff 0%, #e6e8ec 50%, #ffffff 100%); }

  /* footer */
  .footer { left: 0; top: 1113px; width: 882px; height: 87px; background: var(--navy); color: #fff; font-family: "Open Sans", sans-serif; }
  .footer-links { left: 97px; top: 28px; font-size: 10px; }
  .footer-links a { color: #fff; text-decoration: none; }
  .footer-links .sep { margin: 0 4px; }
  .copyright { left: 97px; top: 51px; font-size: 8.6px; color: #d6dbe6; }
  .follow { left: 662px; top: 22px; font-size: 10px; }
  .social { left: 659px; top: 46px; display: flex; gap: 4px; }
  .social span { width: 22px; height: 22px; border-radius: 50%; background: #fff; }
</style>
</head>
<body>

<header>
  <div class="abs brand">Harbin Blue Torch<small>DIVISION</small></div>
  <div class="abs search">
    <svg width="10" height="10" viewBox="0 0 10 10"><circle cx="4" cy="4" r="3" fill="none" stroke="#666" stroke-width="1.4"/><line x1="6.3" y1="6.3" x2="9.3" y2="9.3" stroke="#666" stroke-width="1.6"/></svg>
  </div>
  <nav class="abs nav">
    <a class="current" href="#">HOME</a>
    <a class="item" href="#">ABOUT</a>
    <a class="item" href="#">PRODUCTS</a>
    <a class="item" href="#" style="margin-right:27px">SOLUTIONS</a>
    <a class="item" href="#">CONTACT US</a>
  </nav>
</header>

<section>
  <div class="abs hero" role="img" aria-label="Photo of a businessman in a suit with an umbrella and briefcase walking along a stormy beach"></div>
  <div class="abs hero-figure" role="img" aria-label="Silhouette area of the walking businessman"></div>
  <div class="abs hero-label one">A DIVISION OF</div>
  <div class="abs hero-label two">HARBINFIELD PTY LTD</div>
  <a class="abs quote-btn" href="#">
    <span class="ico"><svg width="10" height="10" viewBox="0 0 10 10"><rect x="1" y="2" width="7" height="7" fill="none" stroke="#333" stroke-width="1.2"/><line x1="4" y1="6" x2="9" y2="1" stroke="#333" stroke-width="1.4"/></svg></span>
    <span class="txt">Request a Quote</span>
  </a>
  <div class="abs dots"><span></span><span class="on"></span><span></span><span></span></div>
</section>

<section>
  <h2 class="abs section-title welcome-title">Welcome to <em>Harbin Blue Torch</em></h2>
  <p class="abs welcome-copy">Harbin Blue Torch provides safety related products, systems and services for the protection of people and property. Utilising world leading technologies for remote monitoring, collection of data and control of public warning infrastructure we are able to greatly improve situational awareness and help reduce the risk of injury and loss of life during emergency related events. Whether for general public warning or site specific applications we have the technology, expertise and experience to help you.</p>
  <a class="abs btn download-btn" href="#">
    <svg width="10" height="10" viewBox="0 0 10 10"><path d="M5 0v6M2.5 3.8L5 6.4 7.5 3.8" fill="none" stroke="#333" stroke-width="1.5"/><rect x="1" y="8" width="8" height="1.6" fill="#333"/></svg>
    Download Brochures
  </a>

  <aside class="abs sectors">
    <h3>
      <svg width="20" height="18" viewBox="0 0 20 18"><path d="M2 7h4l9-5v13l-9-5H2z" fill="#d9312b"/><rect x="4" y="10" width="3" height="6" fill="#d9312b"/></svg>
      <span><em>Market</em> Sectors</span>
    </h3>
    <ul>
      <li>Environmental</li>
      <li>Mining</li>
      <li>Oil and Gas</li>
      <li>Construction and Transport</li>
      <li>Public Health and Safety</li>
    </ul>
  </aside>

  <div class="abs divider"></div>
</section>

<section>
  <h2 class="abs section-title featured-title">Featured <em>Products</em></h2>
  <p class="abs featured-sub">Disaster Management Products &amp; Solutions</p>
  <div class="pager">
    <span class="prev"><svg width="6" height="8" viewBox="0 0 6 8"><path d="M5 0L1 4l4 4" fill="none" stroke="#999" stroke-width="1.2"/></svg></span>
    <span class="next"><svg width="6" height="8" viewBox="0 0 6 8"><path d="M1 0l4 4-4 4" fill="none" stroke="#fff" stroke-width="1.4"/></svg></span>
  </div>

  <article class="abs card" style="left:95px">
    <div class="photo sirens" role="img" aria-label="Photo of a tall outdoor warning siren against blue sky"></div>
    <h4>SIRENS</h4>
    <p>We are the only Australian distributor of renowned US-made</p>
    <a class="btn buy" href="#">Buy Online</a>
  </article>
  <article class="abs card" style="left:272px">
    <div class="photo signage" role="img" aria-label="Photo of a large yellow mining haul truck"></div>
    <h4>SIGNAGE</h4>
    <p>We are the only Australian distributor of renowned US-made</p>
    <a class="btn buy" href="#">Buy Online</a>
  </article>
  <article class="abs card" style="left:449px">
    <div class="photo cameras" role="img" aria-label="Photo of a motorcyclist on a flood-damaged country road"></div>
    <h4>CAMERAS</h4>
    <p>We are the only Australian distributor of renowned US-made</p>
    <a class="btn buy" href="#">Buy Online</a>
  </article>
  <article class="abs card" style="left:626px">
    <div class="photo monitoring" role="img" aria-label="Photo of tablets and phone showing monitoring maps and dashboards"></div>
    <h4>MONITORING</h4>
    <p>We are the only Australian distributor of renowned US-made</p>
    <a class="btn buy" href="#">Buy Online</a>
  </article>
</section>

<footer class="abs footer">
  <div class="abs footer-links"><a href="#">Home</a><span class="sep">/</span><a href="#">About</a><span class="sep">/</span><a href="#">Contact Us</a><span class="sep">/</span><a href="#">Terms of Website Use</a></div>
  <div class="abs copyright">© Harbinfield 2014. Site by Nexa Studio.</div>
  <div class="abs follow">Follow Us</div>
  <div class="abs social"><span></span><span></span><span></span><span></span><span></span></div>
</footer>

</body>
</html>
```